Sale PPC Banner Ad Design Update

We need some Brixel PPC Banner Ad's for our sale altered to include product shots in the background. Attached are some examples that we currently use. We want a similar format/look but with the attached product shots used as the background image. Product image is called "PLXOve Tier 4"

Have also included our logo file as well.

Industry/Entity Type

Brixel

Font styles to use
Sans Serif

Requirements
Must have
• The must-have sizes (up to 150kb):
• • Banner: 468 x 60
• • Large mobile banner 320 x 100
• • Leaderboard: 728 x 90
• • Square: 250 x 250
• • Small square: 200 x 200
• • Large rectangle: 336 x 280
Nice to have
• The nice-to-have sizes:
• • Vertical rectangle: 240 x 400
• • Mobile leaderboard: 320 x 50
• • Inline rectangle: 300 x 250
• • Skyscraper: 120 x 600
• • Wide skyscraper: 160 x 600
• • Half-page: 300 x 600
• • Large leaderboard: 970 x 90
• • Billboard: 970 x 250
• • Portrait: 300 x 1050

```html
<!DOCTYPE html>
<html lang="en">
<head>
<meta charset="utf-8">
<title>Brixel Luxury Shoes Sale Banner</title>
<link href="https://fonts.googleapis.com/css2?family=Lato:wght@300;400;700&display=swap" rel="stylesheet">
<style>
  :root {
    --paper: #ffffff;
    --ink: #111111;
    --headline-gold: #cdb97c;
    --copy-white: #f4f1ea;
    --scene-deep: #1a1620;
    --scene-red: #5a1a22;
    --scene-navy: #1c2440;
    --scene-gold: #4a3d1a;
  }
  html, body {
    margin: 0;
    padding: 0;
    width: 1200px;
    height: 309px;
    overflow: hidden;
    background: var(--paper);
  }
  .banner {
    position: relative;
    width: 1200px;
    height: 309px;
    overflow: hidden;
    font-family: "Lato", sans-serif;
  }
  .brand-strip {
    position: absolute;
    left: 0;
    top: 0;
    width: 114px;
    height: 309px;
    background: var(--paper);
  }
  .brand-name {
    position: absolute;
    left: 57px;
    top: 154px;
    transform: translate(-50%, -50%) rotate(-90deg);
    font-family: "Lato", sans-serif;
    font-weight: 400;
    font-size: 74px;
    line-height: 1;
    color: var(--ink);
    white-space: nowrap;
    letter-spacing: 1px;
  }
  .product-scene {
    position: absolute;
    left: 114px;
    top: 0;
    width: 1086px;
    height: 309px;
    background:
      radial-gradient(ellipse at 20% 70%, var(--scene-red) 0%, transparent 55%),
      radial-gradient(ellipse at 75% 30%, var(--scene-navy) 0%, transparent 60%),
      radial-gradient(ellipse at 90% 85%, var(--scene-gold) 0%, transparent 50%),
      linear-gradient(100deg, var(--scene-deep) 0%, #2a1c26 45%, var(--scene-deep) 100%);
  }
  .sale-copy {
    position: absolute;
    left: 597px;
    top: 0;
    transform: translateX(-50%);
    text-align: center;
    white-space: nowrap;
  }
  .sale-kicker {
    position: absolute;
    left: 50%;
    top: 62px;
    transform: translateX(-50%);
    font-weight: 400;
    font-size: 22px;
    letter-spacing: 2.5px;
    color: var(--copy-white);
  }
  .sale-headline {
    position: absolute;
    left: 50%;
    top: 88px;
    transform: translateX(-50%);
    font-weight: 300;
    font-size: 80px;
    line-height: 1;
    letter-spacing: 10px;
    color: var(--headline-gold);
  }
  .sale-cta {
    position: absolute;
    left: 50%;
    top: 180px;
    transform: translateX(-50%);
    font-weight: 700;
    font-size: 22px;
    letter-spacing: 2.5px;
    color: var(--copy-white);
  }
</style>
</head>
<body>
  <div class="banner">
    <div class="brand-strip">
      <span class="brand-name">Brixel</span>
    </div>
    <div class="product-scene" role="img" aria-label="Close-up of two-tone black and white PLXOve Tier 4 penny loafers worn with patterned trousers, standing on a colourful red, yellow and blue geometric rug"></div>
    <div class="sale-copy">
      <div class="sale-kicker">LUXURY SHOES</div>
      <div class="sale-headline">SALE</div>
      <div class="sale-cta">SHOP NOW</div>
    </div>
  </div>
</body>
</html>
```